Whale Watching Voucher(ticket) Layout

Tidalroam.com.au would like a new design for their existing vouchers (tickets) being issued when a customer completes a purchase.
These vouchers are to be issued from within Salesforce CRM using Conga Composer (don't worry about that, we'll handle that) but that does mean that the voucher template needs to be designed and provided in Microsoft Word. The voucher will be sent via an email and we require a HTML email design also.
The following fields need to be included on the email/Voucher:
BOOKING CONFIRMATION NUMBER (e&v)
First Name (e&v)
Tour Name (e&v)
Tour Operator Name (e&v)
Telephone Contact (e&v)
Departure Date (e&v)
Party Name (e&v)
Adults Tickets (v)
Concession Tickets (v)
Child Tickets (v)
Infant Tickets (v)
Pickup Location (v)
Pickup Time (v)
Boarding Place (v)
Boarding Time (v)
Departure Time (v)
Return Time (v)
Terms and conditions (e&v) - this is quite a long description
What to Bring (v) - this is quite a long description
What to do if the Pick-up is more than 10 mins late (v) - this is a long description
What to do if you're late (v) - this is quite a long description
Booking Terms and Conditions
{!Opportunity.Tour_Terms_and_Conditions_PG1__c}
FREECALL 1800 437 962 (Australia)
International +61 7 5926 8174
Skype journeymoss
(e&v indicate fields to be included on the Email and the Voucher)
(v indicate fields to be included on the Voucher only)
Updates
Project Deadline Extended
Reason: I realised the original Deadline didn't take weekends into account so have extended it to the end of this week. The Whale season is well underway so need to have it completed by Friday. Thanks all for your efforts.
I uploaded the current (text based) samples of the email & voucher that we are hoping you are going to be able to redesign for us.
Sorry for lack of feedback, I got caught up on another project. We are reviewing the designs tomorrow and will get back to you all.
Target Market(s)
Mid market Australian and International Tourists
Industry/Entity Type
Purchase
Requirements
Must have
- Consistency with existing Tidalroam.com.au & coralpath.com.au branding.
The Voucher should be designed to be printed out on a single A4 sheet.
Nice to have
- It would be good to have a paragraph/section referencing the coralpath.com.au logo and website on the email (not the voucher).
Any recommendation for additional information/fields that should/could be included not listed above will be gratefully received.
Happy for you to reword the labels to make them more friendly.

```html
<!DOCTYPE html>
<html lang="en">
<head>
<meta charset="utf-8">
<title>Tidalroam Tour Voucher</title>
<link href="https://fonts.googleapis.com/css2?family=Arimo:wght@400;700&display=swap" rel="stylesheet">
<style>
:root{
  --ink:#1d1d1d;
  --body:#333;
  --teal:#2aa79b;
  --green:#4f9a44;
  --sea-wash:#d3ece7;
  --leaf-wash:#dcedd3;
  --frame:#555;
  --paper:#fff;
}
*{box-sizing:border-box;margin:0;padding:0}
html,body{width:861px;height:1200px;overflow:hidden;background:var(--paper)}
.voucher{position:relative;width:861px;height:1200px;border:1px solid var(--frame);font-family:"Arimo",Arial,sans-serif;color:var(--ink);overflow:hidden}
.backdrop{position:absolute;border-radius:50%}
.backdrop--sea{left:262px;top:190px;width:440px;height:405px;background:var(--sea-wash)}
.backdrop--leaf{left:240px;top:780px;width:440px;height:400px;background:var(--leaf-wash)}
.brand{position:absolute;left:42px;display:flex;align-items:center;gap:8px;font-size:13px;font-weight:700;letter-spacing:.2px}
.brand__dot{width:36px;height:36px;border-radius:50%}
.brand--sea{top:42px;color:var(--teal)}
.brand--sea .brand__dot{background:var(--teal)}
.brand--leaf{top:92px;color:var(--green)}
.brand--leaf .brand__dot{background:var(--green)}
.photo{position:absolute;border:1px solid #fff;box-shadow:0 0 1px rgba(0,0,0,.3)}
.fields{position:absolute;left:40px;width:384px;font-size:16px;line-height:19.8px;list-style:none}
.fields--booking{top:234px}
.fields--transfer{top:457px}
.fields li{display:flex;align-items:baseline;gap:8px;white-space:nowrap}
.fields li::after{content:"";flex:1;border-bottom:1.5px dotted #444;transform:translateY(-3px)}
.info{position:absolute;left:250px;top:740px;width:578px;font-size:11px;line-height:14.3px;color:var(--body);text-align:justify}
.info p{text-indent:30px;margin-bottom:13px}
.info p:nth-of-type(3){margin-bottom:16px}
.info b{color:var(--ink)}
.contact{position:absolute;left:40px;top:1127px;font-size:11px;line-height:14.5px;color:var(--body)}
</style>
</head>
<body>
<main class="voucher">
  <div class="backdrop backdrop--sea"></div>
  <div class="backdrop backdrop--leaf"></div>

  <div class="brand brand--sea"><span class="brand__dot"></span>Tidalroam</div>
  <div class="brand brand--leaf"><span class="brand__dot"></span>Coralpath</div>

  <div class="gallery gallery--sea">
    <div class="photo" role="img" aria-label="Ocean spray photo" style="left:282px;top:148px;width:18px;height:40px;transform:rotate(30deg);background:#3a6fa8"></div>
    <div class="photo" role="img" aria-label="Deep blue sea photo" style="left:318px;top:98px;width:40px;height:34px;transform:rotate(-35deg);background:#2d5f9a"></div>
    <div class="photo" role="img" aria-label="Whale breaching photo" style="left:372px;top:64px;width:42px;height:42px;transform:rotate(-25deg);background:#3f6e9c"></div>
    <div class="photo" role="img" aria-label="Whale tail photo" style="left:428px;top:38px;width:48px;height:42px;transform:rotate(-15deg);background:#1f4f8a"></div>
    <div class="photo" role="img" aria-label="Yellow tour boat photo" style="left:493px;top:22px;width:48px;height:50px;transform:rotate(-5deg);background:#c9a937"></div>
    <div class="photo" role="img" aria-label="Catamaran at sea photo" style="left:557px;top:24px;width:50px;height:56px;transform:rotate(6deg);background:#5a7fa8"></div>
    <div class="photo" role="img" aria-label="Vessel deck photo" style="left:612px;top:38px;width:52px;height:60px;transform:rotate(15deg);background:#7a93ac"></div>
    <div class="photo" role="img" aria-label="Tour vessel underway photo" style="left:662px;top:64px;width:54px;height:60px;transform:rotate(24deg);background:#5d7f9c"></div>
    <div class="photo" role="img" aria-label="Boat at marina photo" style="left:702px;top:104px;width:62px;height:60px;transform:rotate(30deg);background:#6b87a0"></div>
    <div class="photo" role="img" aria-label="Harbour cruise photo" style="left:732px;top:162px;width:62px;height:58px;transform:rotate(20deg);background:#8ba0b3"></div>
    <div class="photo" role="img" aria-label="Whale in blue water photo" style="left:752px;top:226px;width:62px;height:52px;transform:rotate(10deg);background:#2f6fb5"></div>
    <div class="photo" role="img" aria-label="Guests watching whales photo" style="left:764px;top:292px;width:62px;height:48px;transform:rotate(5deg);background:#4f7fa8"></div>
    <div class="photo" role="img" aria-label="Yellow boat deck photo" style="left:766px;top:350px;width:60px;height:46px;transform:rotate(4deg);background:#d4b83a"></div>
    <div class="photo" role="img" aria-label="Red tour boat photo" style="left:758px;top:404px;width:60px;height:46px;transform:rotate(16deg);background:#c2383e"></div>
    <div class="photo" role="img" aria-label="Boat wake photo" style="left:734px;top:458px;width:58px;height:46px;transform:rotate(26deg);background:#8aa2b8"></div>
  </div>

  <ul class="fields fields--booking">
    <li>First Name</li>
    <li>Tour Name</li>
    <li>Tour Operator Name</li>
    <li>Telephone Contact</li>
    <li>Departure Date</li>
    <li>Party Name</li>
    <li>Adults Tickets</li>
    <li>Concession Tickets</li>
    <li>Child Tickets</li>
    <li>Infant Tickets</li>
  </ul>
  <ul class="fields fields--transfer">
    <li>Pickup Location</li>
    <li>Pickup Time</li>
    <li>Boarding Place</li>
    <li>Boarding Time</li>
    <li>Departure Time</li>
    <li>Return Time</li>
  </ul>

  <div class="gallery gallery--leaf">
    <div class="photo" role="img" aria-label="Rainforest photo" style="left:505px;top:690px;width:40px;height:30px;transform:rotate(30deg);background:#3e6b33"></div>
    <div class="photo" role="img" aria-label="Lagoon photo" style="left:450px;top:650px;width:46px;height:40px;transform:rotate(22deg);background:#7fb7c4"></div>
    <div class="photo" role="img" aria-label="Beach walk photo" style="left:393px;top:622px;width:50px;height:52px;transform:rotate(12deg);background:#8b9a76"></div>
    <div class="photo" role="img" aria-label="Tall forest photo" style="left:325px;top:612px;width:48px;height:56px;transform:rotate(3deg);background:#4b6b3a"></div>
    <div class="photo" role="img" aria-label="Coastal headland photo" style="left:258px;top:615px;width:50px;height:55px;transform:rotate(-6deg);background:#3f7fb4"></div>
    <div class="photo" role="img" aria-label="Forest track photo" style="left:195px;top:628px;width:52px;height:58px;transform:rotate(-15deg);background:#3c5e30"></div>
    <div class="photo" role="img" aria-label="White sand lake photo" style="left:136px;top:655px;width:58px;height:60px;transform:rotate(-25deg);background:#8cc6d9"></div>
    <div class="photo" role="img" aria-label="Rainforest walk photo" style="left:90px;top:702px;width:56px;height:64px;transform:rotate(-33deg);background:#56703f"></div>
    <div class="photo" role="img" aria-label="Beach drive photo" style="left:56px;top:758px;width:60px;height:58px;transform:rotate(-40deg);background:#a9bfae"></div>
    <div class="photo" role="img" aria-label="Shipwreck on beach photo" style="left:30px;top:816px;width:62px;height:50px;transform:rotate(-6deg);background:#7d8fa6"></div>
    <div class="photo" role="img" aria-label="Couple on beach photo" style="left:22px;top:880px;width:60px;height:46px;transform:rotate(4deg);background:#8fae8f"></div>
    <div class="photo" role="img" aria-label="Ocean beach photo" style="left:24px;top:940px;width:62px;height:46px;transform:rotate(2deg);background:#4d8cc2"></div>
    <div class="photo" role="img" aria-label="Forest boardwalk photo" style="left:42px;top:1000px;width:60px;height:46px;transform:rotate(10deg);background:#5b7a3c"></div>
    <div class="photo" role="img" aria-label="Fern gully photo" style="left:76px;top:1050px;width:52px;height:46px;transform:rotate(22deg);background:#44672f"></div>
  </div>

  <section class="info">
    <p><b>Terms and condition:</b> m dolor sit amet, consectetuer adipiscing elit. nam cursus. morbi ut mi. nullam enim leo, egestas condimentum at, laoreet mattis, massa. sed eleifend nonummy diam. praesent mauris ante, elemum et, bibendum at, posuere sit amet, nibh. duis tincidunt lectus quis dui viverra vestibulum. suspendsse vulputate aliquam dui. nulla elementum dui ut augue. aliquam vehicula mi at mauris. maecenas placerat, nisl at consequat rhoncus, sem nunc gravida justo, quis eleifend arcu velit quis lacus. morbi magn magna, tincidunt a, mattis non, imperdiet vitae, tellus. sed odio est, auctor ac, sollicitudin in, consequat vitae, orci. fusce id felis. vivamus sollicitudin metus eget eros.</p>
    <p><b>What to bring</b>: lorem ipsum dolor sit amet, consectetuer adipiscing elit. nam cursus. morbi ut mi. nullam enim leo, egestas id, condimentum at, laoreet mattis, massa. sed eleifend nonummy diam. praesent mauris ante, elementum et, bibendum at, posuere sit amet, nibh. duis tincidunt lectus quis dui viverra vestibulum. suspendisse vulputate aliquam dui. nulla elementum dui ut augue. aliquam vehicula mi at mauris. maecenas placerat, nisl at consequat rhoncus, sem nunc gravida justo, quis eleifend arcu velit quis lacus. morbi magna magna, tincidunt a, mattis non, imperdiet vitae, tellus. sed odio est, auctor ac, sollicitudin in, consequat vitae, orci. fusce id felis. vivamus sollicitudin metus eget eros.</p>
    <p><b>What to do if the Pick-up is more than 10 mins late</b>: lorem ipsum dolor sit amet, morbi ut mi. nullam enim leo, egestas id, condimentum at, laoreet mattis, massa. sed eleifend nonummy diam. praesent mauris ante, elementum et, bibendum at, posuere sit amet, nibh. duis tincidunt lectus quis dui viverra vestibulum. suspendisse vulputate aliquam dui. nulla elementum dui ut augue. aliquam vehicula mi at mauris. maecenas placerat, nisl at consequat rhoncus, sem nunc gravida justo, quis eleifend arcu velit quis lacus. morbi magna magna, tincidunt a, mattis non, imperdiet vitae, tellus. sed odio est, auctor ac, sollicitudin in, consequat vitae, orci. fusce id felis. vivamus sollicitudin metus eget eros.</p>
    <p><b>What to doif you are late</b>: loremlorem lorem lorem ipsum dolor sit amet, morbi ut mi. nullam enim leo, egestas id, condimentum at, laoreet mattis, massa. sed eleifend nonummy diam. praesent mauris ante, elementum et, bibendum at, posuere sit amet, nibh. duis tincidunt lectus quis dui viverra vestibulum. suspendisse vulputate aliquam dui. nulla elementum dui ut augue. aliquam vehicula mi at mauris. maecenas placerat, nisl at consequat rhoncus, sem nunc gravida justo, quis eleifend arcu velit quis lacus. morbi magna magna, tincidunt a, mattis non, imperdiet vitae, tellus. sed odio est, auctor ac, sollicitudin in, consequat vitae, orci. fusce id felis. vivamus sollicitudin metus eget eros.</p>
  </section>

  <address class="contact" style="font-style:normal">
    FREECALL 1800 437 962 (Australia)<br>
    International +61 7 5926 8174<br>
    Skype journeymoss
  </address>
</main>
</body>
</html>
```